CTWI application splash screen

We need a 1024x768 image for use as an application splash screen.
The image will be displayed full screen on an 10 inch industrial PC 1024x768 screen while our application is launching. The image should convey that the application is "Waiting for connection to Wi-Fi access point..." and include a graphic of the industrial PC connected to the access point via an Ethernet cable. A list of troubleshooting steps should be included at the bottom of the image. The troubleshooting steps should not be the main focus of the image and should be shown in a smaller font (but still readable at 1024x768 displayed on a 10 inch screen).
I will include a mock up of the general idea of what we are looking for as well as image files for the industrial PC, a screenshot of our application to show on the PC's screen and the AP.
For general look and feel and a sense of corporate branding please review our website https://corvanetillageworks.com/. The splash screen should reflect corporate branding.
Target Market(s)
Users of our application
Industry/Entity Type
Agriculture

```html
<!DOCTYPE html>
<html lang="en">
<head>
<meta charset="utf-8">
<title>CTWI – Waiting for Wi-Fi connection</title>
<link rel="stylesheet" href="https://fonts.googleapis.com/css2?family=Lexend:wght@400;500;600&display=swap">
<style>
  :root {
    --brand-green: #41bc66;
    --white: #ffffff;
    --ink: #1c1c1c;
    --device-dark: #2e3230;
    --ap-tone: #e6e8e6;
    --cable: #111111;
  }
  * { box-sizing: border-box; margin: 0; padding: 0; }
  html, body { width: 1200px; height: 900px; overflow: hidden; }
  body {
    position: relative;
    background: var(--brand-green);
    font-family: "Lexend", sans-serif;
    color: var(--white);
  }
  .brand { position: absolute; left: 38px; top: 42px; }
  .brand-name {
    display: block;
    font-size: 60px; font-weight: 600; line-height: 1; letter-spacing: 2px;
  }
  .brand-tagline {
    display: block; margin-top: 14px;
    font-size: 21px; font-weight: 400; line-height: 1;
  }
  .brand-suffix {
    display: block; margin-top: 4px; padding-left: 150px;
    font-size: 12px; font-weight: 400;
  }
  .headline {
    position: absolute; left: 200px; width: 820px; top: 48px;
    text-align: center; white-space: nowrap;
    font-size: 74px; font-weight: 500; line-height: 82px;
  }
  .diagram { position: absolute; left: 0; top: 0; }
  .device-label { position: absolute; text-align: center; font-weight: 500; }
  .device-label.computer { left: 60px; width: 240px; top: 518px; font-size: 31px; line-height: 30px; }
  .device-label.access-point { left: 820px; width: 360px; top: 516px; font-size: 32px; line-height: 36px; }
  .device-label .model { display: block; font-size: 20px; line-height: 22px; }
  .troubleshooting {
    position: absolute; left: 35px; top: 631px; width: 1133px; height: 234px;
    background: var(--white); border-radius: 24px;
    color: var(--ink); padding: 10px 24px 0 24px;
  }
  .troubleshooting h2 { font-size: 28px; font-weight: 500; line-height: 40px; }
  .troubleshooting ul { list-style: none; font-size: 19px; line-height: 25px; }
  .troubleshooting li.step::before { content: "•"; margin-right: 7px; }
  .troubleshooting ul.sub { padding-left: 43px; padding-right: 30px; }
  .troubleshooting ul.sub li { padding-left: 20px; text-indent: -20px; }
  .troubleshooting ul.sub li::before { content: "→"; display: inline-block; width: 20px; text-indent: 0; font-size: 15px; }
</style>
</head>
<body>
  <div class="brand">
    <span class="brand-name">CTWI</span>
    <span class="brand-tagline">Corvane Tillage Works</span>
    <span class="brand-suffix">Inc.</span>
  </div>

  <h1 class="headline">Waiting for<br>connection to Wi&#8209;Fi<br>access point…</h1>

  <svg class="diagram" width="1200" height="900" viewBox="0 0 1200 900">
    <path d="M318 476 H1102 Q1110 476 1110 468 V456" fill="none" stroke="var(--cable)" stroke-width="4"/>
    <rect role="img" aria-label="Photo of the rugged tractor cab computer showing the seeding application" x="42" y="285" width="280" height="222" rx="16" fill="var(--device-dark)"/>
    <rect role="img" aria-label="Photo of the outdoor Wi-Fi access point" x="1090" y="258" width="40" height="200" rx="6" fill="var(--ap-tone)"/>
  </svg>

  <div class="device-label computer">Tractor cab computer</div>
  <div class="device-label access-point">Wi-Fi Access Point<span class="model">Stratalink AX300-Field</span></div>

  <section class="troubleshooting">
    <h2>Troubleshooting steps:</h2>
    <ul>
      <li class="step">This screen should only be visible for a short time on boot.</li>
      <li class="step">If this screen stays visible for more than a minute:
        <ul class="sub">
          <li>Verify that the Wi-Fi Access Point (AP) powers up when this system does (indicated by a green light on the side of the AP).</li>
          <li>Check the Ethernet cable between this system and the AP for damage, and replace it if necessary.</li>
          <li>Power-cycle this system and wait for it to reboot fully.</li>
          <li>If the issue persists, contact CTWI support for further assistance.</li>
        </ul>
      </li>
    </ul>
  </section>
</body>
</html>
```